Party flyer design

Hi ArtHive,

I need a party flyer designed incorporating my logo and the verbiage stated below for a
social get-together I'm throwing at a local martini bar and lounge in my local area.

I've attached my logo and a copy of a flyer I've seen that incorporates the look and feel I'm looking for.

Thanks

Corvane 9 presents
Weekend Velvet Mixers

Join us Fridays at 11:00 PM - 2:00 AM
at Amber Glass Westmoor
27150 Harwick Loop, Suite 340
Charlotte, NC 28391

For more details email us at info@corvane9.net

```html
<!DOCTYPE html>
<html lang="en">
<head>
<meta charset="utf-8">
<title>Corvane 9 presents Weekend Velvet Mixers</title>
<link rel="stylesheet" href="https://fonts.googleapis.com/css2?family=Josefin+Sans:wght@300;400;600&family=Righteous&family=Great+Vibes&display=swap">
<style>
  :root {
    --bg: #141318;
    --bg-deep: #0c0b10;
    --gold: #f2c44a;
    --gold-light: #fff1b0;
    --gold-dark: #a8701a;
    --frame: #d9a640;
    --orange: #f28a22;
    --white: #f4f1ea;
    --smoke: #6f6b70;
  }
  * { margin: 0; padding: 0; box-sizing: border-box; }
  html, body { width: 846px; height: 1200px; overflow: hidden; background: var(--bg); }
  .flyer {
    position: relative;
    width: 846px;
    height: 1200px;
    overflow: hidden;
    background: radial-gradient(ellipse at 50% 40%, #221c22 0%, var(--bg) 55%, var(--bg-deep) 100%);
    font-family: "Josefin Sans", sans-serif;
    color: var(--white);
  }
  .hero-scene {
    position: absolute;
    inset: 0;
    background:
      radial-gradient(circle 330px at 400px 400px, rgba(255,214,140,.85) 0%, rgba(224,119,45,.55) 25%, rgba(120,60,40,.22) 60%, rgba(120,60,40,0) 100%),
      radial-gradient(circle 260px at 560px 820px, rgba(91,63,176,.38) 0%, rgba(91,63,176,0) 100%);
  }
  .frames { position: absolute; inset: 0; pointer-events: none; }
  .presenter {
    position: absolute;
    top: 24px;
    left: 0;
    width: 100%;
    display: flex;
    justify-content: center;
    align-items: center;
    gap: 16px;
    padding-left: 60px;
    font-weight: 300;
    font-size: 38px;
    letter-spacing: 5px;
    text-transform: uppercase;
  }
  .presenter-name { color: var(--white); padding-top: 6px; }
  .presenter-name .num { color: var(--orange); font-weight: 600; }
  .presenter-mark {
    width: 86px; height: 86px; border-radius: 50%;
    background: var(--orange);
  }
  .title-block { font-size: inherit; font-weight: normal; }
  .title {
    position: absolute;
    left: 0; width: 100%;
    text-align: center;
    font-family: "Righteous", sans-serif;
    text-transform: uppercase;
    line-height: 1;
    background: linear-gradient(180deg, var(--gold-light) 0%, var(--gold) 45%, var(--gold-dark) 100%);
    -webkit-background-clip: text;
    background-clip: text;
    color: transparent;
    filter: drop-shadow(0 3px 2px rgba(0,0,0,.7));
  }
  .title-top { top: 562px; font-size: 74px; letter-spacing: 2px; }
  .title-main { top: 640px; font-size: 122px; letter-spacing: 10px; }
  .invite {
    position: absolute; top: 788px; left: 0; width: 100%;
    text-align: center;
    font-family: "Great Vibes", cursive;
    font-size: 70px;
    line-height: 1;
    color: var(--white);
  }
  .schedule {
    position: absolute; top: 868px; left: 0; width: 100%;
    text-align: center;
    font-family: "Righteous", sans-serif;
    font-size: 35px;
    line-height: 1;
    letter-spacing: 3px;
    text-transform: uppercase;
    color: var(--gold);
    text-shadow: 0 2px 3px rgba(0,0,0,.8);
  }
  .venue {
    position: absolute; top: 972px; left: 0; width: 100%;
    text-align: center;
    font-style: normal;
    font-size: 23px;
    line-height: 32px;
    letter-spacing: 1.5px;
    text-transform: uppercase;
    color: var(--white);
  }
  .contact {
    position: absolute; top: 1091px; left: 0; width: 100%;
    text-align: center;
    font-weight: 300;
    font-size: 20px;
    letter-spacing: 1.5px;
    text-transform: uppercase;
    color: var(--gold);
  }
</style>
</head>
<body>
<main class="flyer">
  <div class="hero-scene" role="img" aria-label="Hip-hop dancer in a green hoodie leaping amid splashing golden drinks, shattering glass and light flares"></div>

  <svg class="frames" width="846" height="1200" viewBox="0 0 846 1200" aria-hidden="true">
    <defs>
      <filter id="soft-blur"><feGaussianBlur stdDeviation="6"/></filter>
    </defs>
    <g fill="none" stroke="var(--frame)" stroke-width="6" stroke-linejoin="miter" opacity=".9">
      <polyline points="0,345 430,272"/>
      <polyline points="470,262 805,240 555,945 250,720"/>
      <line x1="0" y1="345" x2="180" y2="540"/>
    </g>
    <g fill="none" stroke="#e3b553" stroke-width="5">
      <polygon points="150,160 240,150 200,220"/>
      <polygon points="440,300 520,340 470,390"/>
    </g>
    <circle cx="780" cy="150" r="66" fill="var(--smoke)" opacity=".4" filter="url(#soft-blur)"/>
  </svg>

  <header class="presenter">
    <span class="presenter-name">Corvane <span class="num">9</span> Presents</span>
    <span class="presenter-mark" aria-hidden="true"></span>
  </header>

  <h1 class="title-block">
    <span class="title title-top">Weekend Velvet</span>
    <span class="title title-main">Mixers</span>
  </h1>

  <p class="invite">Join us</p>
  <p class="schedule">Fridays @ 11:00PM - 2:00AM</p>

  <address class="venue">
    At Amber Glass Westmoor<br>
    27150 Harwick Loop, Suite 340<br>
    Charlotte, NC 28391
  </address>

  <p class="contact">For more details email us at info@corvane9.net</p>
</main>
</body>
</html>
```